MBA Banner Online Ad

I represent the MBA program department of China's #1 global business school, TOVRA. www.tovra.edu. We are looking for a designer to offer something unique, out of the box, yet maintaining the branding and reputation of our school. Our goal is to build a long-term relationship with our chosen designer for all the our department's design needs. The designer should provide amazing creativity, professionalism, and competitive pricing.

We are currently looking to design a flas banner add for MBA websites around the world with the following message. Add size is 300x350 pixels:

"In 1275 Edmund Varr set out to travel the world to discover China" Banner 1st Page

"Now is your chance to live and learn in China in order to discover the world" Banner 2nd Page

"TOVRA MBA - experience an elite business school with a new perspective" Banner 3rd Page

Our Logo and motto: "Rooted Minds, Open Horizons"

We need an add reflecting Edmund Varrs travels or Edmund Varr himself along with modern photos of Shanghai or our university, or whatever you suggest to reflect the message of modernity, elite organization, etc.

Please go according to our guidlines in the provided attachments.

Looking forward to your offers!
Updates

Current ad featured on :   http://lanternandledger.com/category/mba-rankings/

Want it replaced by a more creative and bold banner.

Project Deadline Extended
Reason: Awaiting a few more replies. Thanks

Target Market(s)

Prospective MBA Students

Industry/Entity Type

Travel

Requirements
Must have
• Color, fonts, etc, should go according to attached guidelines in the attachments provided. Please contact me directly should you have any questions or need any clarifications.

Ned

```html
<!DOCTYPE html>
<html lang="en">
<head>
<meta charset="utf-8">
<title>TOVRA MBA Banner</title>
<link rel="stylesheet" href="https://fonts.googleapis.com/css2?family=Roboto+Condensed:wght@700;800&display=swap">
<style>
  :root {
    --frame: #8a8a8a;
    --red-deep: #8c1d2c;
    --red-mid: #b23a4c;
    --red-soft: #d9848f;
    --pink-light: #efc3c7;
    --white: #ffffff;
    --shadow: rgba(60, 10, 20, 0.85);
    --motto-fill: #8e1e2d;
    --motto-gold: #f4e21c;
    --logo-red: #a3202f;
  }
  * { margin: 0; padding: 0; box-sizing: border-box; }
  html, body { width: 1200px; height: 600px; overflow: hidden; background: #ffffff; }
  .banner {
    position: relative;
    width: 1200px;
    height: 600px;
    border: 5px solid var(--frame);
    overflow: hidden;
    font-family: "Roboto Condensed", "Arial Narrow", sans-serif;
  }
  .scene {
    position: absolute;
    inset: 0;
    background:
      radial-gradient(ellipse 420px 360px at 1010px 260px, rgba(240,200,205,0.85), rgba(240,200,205,0) 70%),
      radial-gradient(ellipse 380px 260px at 110px 560px, rgba(255,240,242,0.95), rgba(255,240,242,0) 70%),
      linear-gradient(180deg, rgba(0,0,0,0) 55%, rgba(226,150,158,0.7) 100%),
      linear-gradient(90deg, var(--red-mid) 0%, var(--red-deep) 40%, var(--red-deep) 60%, var(--red-soft) 100%);
  }
  .globe {
    position: absolute;
    left: 800px;
    top: 150px;
    width: 300px;
    height: 300px;
    border-radius: 50%;
    background: radial-gradient(circle at 40% 35%, #f4eef0 0%, #b9bfcc 45%, #6d7488 80%, #4d5264 100%);
    opacity: 0.9;
  }
  .globe-label {
    position: absolute;
    left: 845px;
    top: 255px;
    font-weight: 800;
    font-size: 56px;
    letter-spacing: 3px;
    color: var(--logo-red);
    opacity: 0.85;
  }
  .headline {
    position: absolute;
    left: 0;
    width: 1170px;
    top: 118px;
    text-align: center;
    color: var(--white);
    font-weight: 700;
    font-size: 48px;
    line-height: 68px;
    letter-spacing: 1.5px;
    text-transform: uppercase;
    text-shadow: 2px 2px 0 var(--shadow), -1px -1px 0 var(--shadow), 1px -1px 0 var(--shadow), -1px 1px 0 var(--shadow);
  }
  .brand {
    position: absolute;
    left: 32px;
    top: 508px;
    display: flex;
    align-items: center;
    gap: 12px;
  }
  .brand-square {
    width: 34px;
    height: 34px;
    background: var(--logo-red);
  }
  .brand-name {
    font-weight: 700;
    font-size: 40px;
    letter-spacing: 2px;
    color: var(--logo-red);
  }
  .motto {
    position: absolute;
    left: 490px;
    top: 512px;
    width: 692px;
    height: 66px;
    background: var(--motto-fill);
    border: 4px solid var(--motto-gold);
    border-radius: 6px;
    display: flex;
    align-items: center;
    justify-content: center;
    color: var(--motto-gold);
    font-weight: 700;
    font-size: 40px;
    letter-spacing: 1px;
    text-transform: uppercase;
  }
</style>
</head>
<body>
  <div class="banner">
    <div class="scene" role="img" aria-label="Red-tinted photograph of a businessman with a briefcase climbing stone steps, and open hands holding a glass globe"></div>
    <div class="globe" role="img" aria-label="Glass globe held in open hands"></div>
    <div class="globe-label">MBA</div>
    <h1 class="headline">In 1275 Edmund Varr set out to travel<br>the world to discover China</h1>
    <div class="brand">
      <span class="brand-square"></span>
      <span class="brand-name">TOVRA</span>
    </div>
    <p class="motto">Rooted Minds, Open Horizons</p>
  </div>
</body>
</html>
```